Letterhead design for Sleep Consulting Business

I'm looking for a new letterhead (heading/footer) design for my Sleep Consulting Business, I work with families to help their children improve their sleep.

The heading/footer will used in Microsoft Word Only-to be used for all of my documents such as writing Sleep Plans. I need to utilize as much working space in the document as possible. This will NOT be printed out on paper- it will only be used for heading/footer on microsoft word, then emailed to clients, who may print it at home.

My brand colors:
Dark Blue Hex: 1F2A42
Lighter Blueish Hex: 90BEC9
You're welcome to check out my website for inspiration- it is freshly created with other colors as well, and I love the outcome. www.hollowpinerest.com

Target Market(s)

Tired parents

Font styles to use
Script
Other font styles liked:
• Great Vibe, Lato or Just Another Hand are all used currently for my brand. Open to other options.

Requirements
Must have
• The letterhead (heading/footer) MUST be kept narrow (height-wise), so I have plenty of space on my document, while including important information.

It should look professional on screen, and when printed.

Must include my business name OR logo (Hollow Pine Sleep Consulting), and my email address. Mara@hollowpinerest.com

Website is optional, not required, just if you need to fill in a spot: www.hollowpinerest.com

```html
<!DOCTYPE html>
<html lang="en">
<head>
<meta charset="utf-8">
<title>Hollow Pine Sleep Consulting – Letterhead</title>
<link rel="stylesheet" href="https://fonts.googleapis.com/css2?family=Source+Sans+3:wght@400;600;700&display=swap">
<style>
  :root {
    --navy: #0d1733;
    --brand-blue: #1f2a42;
    --sky: #90bec9;
    --slate: #7d7f95;
    --ink: #2b2b2e;
    --rule: #b9d6dd;
    --paper: #ffffff;
    --backdrop: #e6e6e6;
  }
  * { box-sizing: border-box; margin: 0; padding: 0; }
  html, body {
    width: 1200px; height: 936px; overflow: hidden;
    background: var(--backdrop);
    font-family: "Source Sans 3", sans-serif;
    color: var(--ink);
  }
  .sheet {
    position: absolute; left: 280px; top: 15px;
    width: 640px; height: 906px;
    background: var(--paper);
    box-shadow: 0 2px 10px rgba(0,0,0,0.12);
    overflow: hidden;
  }
  .header-waves { position: absolute; left: 0; top: 0; width: 640px; height: 150px; }
  .brand {
    position: absolute; left: 40px; top: 118px;
    display: flex; align-items: center; gap: 10px;
  }
  .brand-dot { width: 26px; height: 26px; border-radius: 50%; background: var(--brand-blue); }
  .brand-name { font-size: 15px; font-weight: 600; color: var(--brand-blue); letter-spacing: 0.2px; }
  .letter {
    position: absolute; left: 60px; top: 196px; width: 520px;
    font-size: 11.5px; line-height: 1.42;
  }
  .date { font-size: 13px; margin-bottom: 20px; }
  .recipient { font-size: 13px; line-height: 1.35; margin-bottom: 14px; }
  .salutation { font-size: 13px; font-weight: 700; margin-bottom: 14px; }
  .letter p.body { margin-bottom: 20px; }
  .signature {
    display: block; margin: 6px 0 0 auto;
    width: 110px; height: 48px; border-radius: 4px;
    background: linear-gradient(90deg, #f2f2f2, #e4e4e4);
  }
  .footer {
    position: absolute; left: 60px; right: 40px; bottom: 58px;
    display: flex; justify-content: flex-end; gap: 20px;
    font-size: 11px; color: var(--ink);
  }
  .contact { display: flex; align-items: center; gap: 5px; }
  .contact svg { width: 10px; height: 10px; }
  .footer-rule {
    position: absolute; left: 60px; right: 40px; bottom: 46px;
    height: 1px; background: var(--rule);
  }
</style>
</head>
<body>
  <main class="sheet">
    <svg class="header-waves" viewBox="0 0 640 150" preserveAspectRatio="none" aria-hidden="true">
      <path d="M0 104 C150 100 260 82 370 40 C440 14 520 0 640 0 L640 140 C560 60 450 70 360 92 C240 120 120 126 0 128 Z" fill="#8a8ca2"/>
      <path d="M0 88 C140 86 250 68 360 30 C430 6 520 0 640 0 L640 118 C560 50 450 58 350 82 C230 110 110 116 0 116 Z" fill="var(--sky)"/>
      <path d="M0 0 L640 0 L640 100 C560 40 460 40 360 60 C240 84 120 92 0 96 Z" fill="var(--navy)"/>
    </svg>

    <div class="brand">
      <span class="brand-dot"></span>
      <span class="brand-name">Hollow Pine Sleep Consulting</span>
    </div>

    <section class="letter">
      <p class="date">January 12, 2021</p>
      <p class="recipient">Mr. John Doe<br>President<br>AA Corporation<br>111 Street Name, Suite#<br>City, State, 12345</p>
      <p class="salutation">Dear Mr. John,</p>
      <p class="body">Lorem Ipsum is simply dummy text of the printing and typesetting industry. Lorem Ipsum has been the industry's standard dummy text ever since the 1500s, when an unknown printer took a galley of type and scrambled it to make a type specimen book. It has survived not only five centuries, but also the leap into electronic typesetting, remaining essentially unchanged.</p>
      <p class="body">The standard chunk of Lorem Ipsum used since the 1500s is reproduced below for those interested. Sections 1.10.32 and 1.10.33 from "de Finibus Bonorum et Malorum" by Tullianus are also reproduced in their exact original form, accompanied by English versions from the 1914 translation by H. Ravensby.</p>
      <p class="body">Lorem Ipsum is simply dummy text of the printing and typesetting industry. Lorem Ipsum has been the industry's standard dummy text ever since the 1500s, when an unknown printer took a galley of type and scrambled it to make a type specimen book. It has survived not only five centuries, but also the leap into electronic typesetting, remaining essentially unchanged. It was popularised in the</p>
      <div class="signature" role="img" aria-label="Handwritten signature of R. Ellory"></div>
    </section>

    <footer class="footer">
      <span class="contact">
        <svg viewBox="0 0 10 10" aria-hidden="true"><circle cx="5" cy="5" r="5" fill="var(--brand-blue)"/><rect x="2.5" y="3.2" width="5" height="3.6" fill="none" stroke="#fff" stroke-width="0.7"/><path d="M2.5 3.2 L5 5.2 L7.5 3.2" fill="none" stroke="#fff" stroke-width="0.7"/></svg>
        Mara@hollowpinerest.com
      </span>
      <span class="contact">
        <svg viewBox="0 0 10 10" aria-hidden="true"><circle cx="5" cy="5" r="5" fill="var(--brand-blue)"/><circle cx="5" cy="5" r="2.6" fill="none" stroke="#fff" stroke-width="0.7"/><path d="M2.4 5 H7.6 M5 2.4 V7.6" stroke="#fff" stroke-width="0.6"/></svg>
        www.hollowpinerest.com
      </span>
    </footer>
    <div class="footer-rule"></div>
  </main>
</body>
</html>
```